bottle label/ product label for smoothies (ultra fresh)

Please create a bottle label for our smoothies for retail distribution.
It's important that the following key features are clearly stated:

Ultra-fresh

Handmade

No preservatives

Not heat-treated

No added sugar

The base of the product label should be transparent, so that the color and content of the smoothie can be seen clearly.

We are a young, dynamic company. Our values are honesty, ultra-freshness, and authenticity — and we are the only ones producing this type of product in our country. We are positioned in the premium segment.

Design style: Modern, clean, and natural — but not playful or childish.

Example product: Kelu Kelu (Mango, Pineapple, Lemon, Passion Fruit, Orange)

Wenn du möchtest, kann ich auch gleich einen konkreten Vorschlag für das Etikettendesign auf Englisch oder einen Entwurfstext für das Label selbst erstellen. Sag einfach Bescheid!

Target Market(s)

trade - convenience

Industry/Entity Type

trade

Font styles to use
Sans Serif

Requirements
Must have
• sales- features: Ultra-fresh Handmade No preservatives Not heat-treated No added sugar

```html
<!DOCTYPE html>
<html lang="en">
<head>
<meta charset="utf-8">
<title>Verano Organic Raw Juice – Label</title>
<link rel="stylesheet" href="https://fonts.googleapis.com/css2?family=Bebas+Neue&family=Montserrat:wght@400;500;800&family=Poppins:wght@500&display=swap">
<style>
  :root {
    --backdrop: #737373;
    --ink: #ffffff;
    --tag-text: #737373;
  }
  * { margin: 0; padding: 0; box-sizing: border-box; }
  html, body { width: 1200px; height: 687px; overflow: hidden; }
  body {
    background: var(--backdrop);
    color: var(--ink);
    font-family: "Montserrat", sans-serif;
    position: relative;
  }
  .label { position: absolute; left: 300px; top: 60px; width: 600px; height: 567px; }
  .brand-name { position: absolute; left: 0; top: 0; width: 140px; height: 567px; }
  .brand-name text { font-family: "Poppins", sans-serif; font-weight: 500; fill: var(--ink); }

  .info { position: absolute; left: 165px; top: 0; width: 330px; }
  .category {
    position: absolute; top: 132px; left: 0;
    font-weight: 800; font-size: 19px; line-height: 24px; letter-spacing: 0.3px;
  }
  .rule { position: absolute; left: 0; height: 1.5px; background: var(--ink); }
  .rule--short { top: 185px; width: 170px; }
  .rule--full { top: 266px; width: 327px; }
  .rule--size-top { top: 488px; width: 119px; }
  .rule--size-bottom { top: 567px; width: 119px; }

  .flavor-name {
    position: absolute; top: 194px; left: -2px;
    font-family: "Bebas Neue", sans-serif; font-size: 76px; line-height: 68px; letter-spacing: 0.5px;
  }
  .tags { position: absolute; top: 278px; left: 0; display: flex; gap: 12px; }
  .tag {
    background: var(--ink); color: var(--tag-text);
    font-weight: 800; font-size: 16px; line-height: 23px; padding: 0 6px;
  }
  .description { position: absolute; top: 313px; left: 0; font-size: 13px; line-height: 17px; font-weight: 500; }

  .feature {
    position: absolute; display: flex; align-items: center; gap: 4px;
    font-family: "Bebas Neue", sans-serif; font-size: 17px; letter-spacing: 0.4px;
  }
  .feature span { border-bottom: 1.5px solid var(--ink); line-height: 18px; }
  .feature svg { width: 38px; height: 38px; }
  .feature--preservatives { top: 388px; left: 0; }
  .feature--sugar { top: 388px; left: 171px; }
  .feature--heat { top: 441px; left: 0; }

  .volume {
    position: absolute; top: 496px; left: 0;
    font-family: "Bebas Neue", sans-serif; font-size: 44px; line-height: 40px;
  }
  .storage { position: absolute; top: 537px; left: 0; font-size: 11px; line-height: 13px; font-weight: 500; }
</style>
</head>
<body>
  <main class="label">
    <svg class="brand-name" viewBox="0 0 140 567" aria-label="Verano">
      <text transform="translate(133 565) rotate(-90)" font-size="165" textLength="562" lengthAdjust="spacingAndGlyphs">Verano</text>
    </svg>

    <section class="info">
      <p class="category">ORGANIC<br>RAW JUICE</p>
      <div class="rule rule--short"></div>
      <h1 class="flavor-name">FLAVOR NAME</h1>
      <div class="rule rule--full"></div>
      <div class="tags">
        <span class="tag">HANDMADE</span>
        <span class="tag">ULTRA – FRESH</span>
      </div>
      <p class="description">Lorem ipsum dolor sit amet, consectetur<br>adipiscing elit, sed do eiusmod</p>

      <div class="feature feature--preservatives">
        <svg viewBox="0 0 38 38" aria-hidden="true"><circle cx="19" cy="19" r="16" fill="none" stroke="#fff" stroke-width="2"/><path d="M16 10h6M17 10v7l-5 9h14l-5-9v-7" fill="none" stroke="#fff" stroke-width="2" stroke-linejoin="round"/></svg>
        <span>NO PRESERVATIVES</span>
      </div>
      <div class="feature feature--sugar">
        <svg viewBox="0 0 38 38" aria-hidden="true"><circle cx="19" cy="19" r="16" fill="none" stroke="#fff" stroke-width="2"/><rect x="11" y="17" width="7" height="7" fill="#fff"/><rect x="20" y="17" width="7" height="7" fill="#fff"/><rect x="15.5" y="10" width="7" height="6" fill="#fff"/></svg>
        <span>NO ADDED SUGAR</span>
      </div>
      <div class="feature feature--heat">
        <svg viewBox="0 0 38 38" aria-hidden="true"><circle cx="19" cy="19" r="16" fill="none" stroke="#fff" stroke-width="2"/><rect x="15" y="9" width="5" height="15" rx="2.5" fill="none" stroke="#fff" stroke-width="2"/><circle cx="17.5" cy="26" r="4" fill="#fff"/><path d="M24 12v6M27 12v6" stroke="#fff" stroke-width="1.8"/></svg>
        <span>NOT HEAT – TREATED</span>
      </div>

      <div class="rule rule--size-top"></div>
      <p class="volume">12OZ</p>
      <p class="storage">Perishable<br>Keep Refrigerated.</p>
      <div class="rule rule--size-bottom"></div>
    </section>
  </main>
</body>
</html>
```